Business Card Design Project

We need a business card design for a consultancy called 'Maple Ridge'. The design should communicate innovation and professionalism. The colors used should complement our logo. Please include source files for winning design.
Updates

Industry/Entity Type

Business

Colors

Designer to choose colors to be used in the design.

Requirements
Must have
• Card size should be 85mm x 50mm. The back side of the card should be the logo on a black background. The front side should display the name 'Maple Ridge' along with standard information. The front's design should graphically complement the back.
Nice to have
• Any graphical elements in the front the complement the back side (with the logo on a black background) would be a plus.

```html
<!DOCTYPE html>
<html lang="en">
<head>
<meta charset="utf-8">
<title>Maple Ridge — Business Card</title>
<link rel="stylesheet" href="https://fonts.googleapis.com/css2?family=Cinzel:wght@500&family=Questrial&display=swap">
<style>
  :root {
    --backdrop: #d9d6d1;
    --card-black: #070707;
    --card-charcoal: #1a1a1a;
    --amber: #ff6a00;
    --gold: #c9893c;
    --gold-light: #e9a95a;
    --beam: #4a2306;
    --text-light: #f2f2f2;
    --title-yellow: #e8a400;
  }
  * { box-sizing: border-box; margin: 0; padding: 0; }
  html, body { width: 1200px; height: 871px; overflow: hidden; }
  body { background: var(--backdrop); position: relative; font-family: "Questrial", sans-serif; }

  .card {
    position: absolute;
    width: 540px;
    height: 318px;
    border-radius: 4px;
    overflow: hidden;
    box-shadow: 0 14px 30px rgba(0,0,0,0.28);
  }

  /* Logo side */
  .card-back {
    left: 70px; top: 120px;
    background: linear-gradient(160deg, var(--card-charcoal), var(--card-black) 60%);
    display: flex; flex-direction: column; align-items: center; justify-content: center;
    gap: 18px;
  }
  .brand-dot {
    width: 120px; height: 120px; border-radius: 50%;
    background: radial-gradient(circle at 50% 40%, var(--gold-light), var(--gold));
  }
  .brand-name {
    font-family: "Cinzel", serif;
    font-weight: 500;
    font-size: 34px;
    letter-spacing: 1px;
    color: var(--gold);
  }

  /* Details side */
  .card-front {
    left: 590px; top: 433px;
    background: var(--card-black);
  }
  .illustration-area {
    position: absolute;
    left: 0; top: 0;
    width: 270px; height: 100%;
    background: linear-gradient(100deg, var(--amber) 0%, #b84c04 45%, var(--beam) 100%);
  }
  .contact {
    position: absolute;
    right: 30px; top: 96px;
    text-align: right;
    color: var(--text-light);
    font-size: 14px;
    line-height: 1.45;
  }
  .contact-name { font-size: 17px; font-weight: 700; letter-spacing: 0.2px; }
  .contact-title { color: var(--title-yellow); font-size: 14px; margin-bottom: 8px; }
  .contact-address { margin-bottom: 10px; }
  .contact-line { display: flex; justify-content: flex-end; align-items: center; gap: 10px; }
  .contact-line svg { width: 13px; height: 13px; fill: var(--title-yellow); flex: none; }
</style>
</head>
<body>

  <section class="card card-back" aria-label="Card back">
    <div class="brand-dot"></div>
    <div class="brand-name">Maple Ridge</div>
  </section>

  <section class="card card-front" aria-label="Card front">
    <div class="illustration-area" role="img" aria-label="Illustration of an orange lighthouse on rocks casting a light beam"></div>

    <div class="contact">
      <div class="contact-name">Dana Hollis</div>
      <div class="contact-title">Ceo</div>
      <div class="contact-address">Level 2, 118 Harbour Road<br>NSW 2070</div>
      <div class="contact-line">02 9460 2317
        <svg viewBox="0 0 16 16" aria-hidden="true"><path d="M3 1h3l1.5 4-2 1.5a9 9 0 0 0 4 4l1.5-2 4 1.5v3a2 2 0 0 1-2 2A13 13 0 0 1 1 3a2 2 0 0 1 2-2z"/></svg>
      </div>
      <div class="contact-line">02 946 0388
        <svg viewBox="0 0 16 16" aria-hidden="true"><path d="M4 1h8v4H4zM1 6h14v7h-3v2H4v-2H1zm4 4v4h6v-4z"/></svg>
      </div>
      <div class="contact-line">enquiries@mapleridgeco.com
        <svg viewBox="0 0 16 16" aria-hidden="true"><path d="M1 3h14v10H1zm1.5 1.5L8 9l5.5-4.5v-.1h-11z"/></svg>
      </div>
    </div>
  </section>

</body>
</html>
```